Healthcare Recruitment Agency Brochure

We need our current Brochure updated as its old and dated. The brochure will be for our current and potential Clients and should provide all the necessary information regarding our services, but in a well presented, easy reading format which echoes our company Brand. The company supplies Healthcare establishments with trained healthcare Staff which can be in a variety of settings.
UPDATE: Following the submission of many designs we would like to amend the information/content to be included in the brochure and have uploaded additional information. We would like an 8 page booklet with the various sections spread out so as not to look to 'wordy' page 1 Front cover, 2 About Us, 3 Our Service, 4 Our promise, 5 Our Staff, 6 Our Ethos, 7 What Our Clients Say/Testimonials, 8 Contact Us/Back page. Please if using pictures (which is welcomed) steer away from the surgical/doctor type. We mainly provide care to the Elderly within Nursing and Residential Homes and Support Environments. Thanks
Updates

Target Market(s)

Healthcare clientell

Industry/Entity Type

Healthcare

Requirements
Must have
• Pictures, animation, easy reading, informative, tie in with website theme www.carewellstaffline.example
Nice to have
• open to ideas
Should not have
• very long text paragraphs

```html
<!DOCTYPE html>
<html lang="en">
<head>
<meta charset="utf-8">
<title>Carewell Staffline – Our Ethos &amp; Our Suggestions</title>
<link rel="stylesheet" href="https://fonts.googleapis.com/css2?family=Roboto:wght@400;500;700&display=swap">
<style>
  :root {
    --teal: #1aa89a;
    --teal-soft: #bfe6e0;
    --blue: #3b5eab;
    --blue-bar: #2f62a8;
    --ink: #1c1c1c;
    --paper: #ffffff;
    --photo-a: #dfe9f5;
    --photo-b: #b9cde6;
  }
  * { margin: 0; padding: 0; box-sizing: border-box; }
  html, body { width: 1200px; height: 849px; overflow: hidden; background: var(--paper); }
  body { font-family: "Roboto", Arial, sans-serif; color: var(--ink); }
  .spread { position: relative; width: 1200px; height: 849px; }

  .bar { position: absolute; top: 54px; height: 6px; background: var(--blue-bar); }
  .bar--left { left: 0; width: 36px; }
  .bar--right { left: 1164px; width: 36px; }
  .bar--centre {
    left: 150px; width: 899px; height: 7px;
    background: linear-gradient(90deg, #4a79bd 0%, #9fb9de 35%, #ffffff 50%, #9fb9de 65%, #4a79bd 100%);
  }
  .brand {
    position: absolute; top: 50px; display: flex; align-items: center; gap: 5px;
    font-weight: 500; font-size: 11px; color: var(--blue);
  }
  .brand__dot { width: 8px; height: 8px; border-radius: 50%; background: var(--teal); }
  .brand--left { left: 47px; }
  .brand--right { left: 1058px; }

  .page-title {
    position: absolute; top: 90px; font-size: 23px; font-weight: 700; color: var(--teal);
  }
  .page-title--ethos { left: 55px; }
  .page-title--suggestions { left: 655px; }
  .rule { position: absolute; top: 107px; height: 4px; background: var(--teal-soft); border-top: 1px solid var(--teal); }
  .rule--ethos { left: 164px; width: 381px; }
  .rule--suggestions { left: 827px; width: 318px; }

  .heading {
    font-size: 14.5px; font-weight: 700; color: var(--blue); letter-spacing: .1px; line-height: 18px;
  }
  .body { font-size: 12px; line-height: 14.6px; }

  .value { position: absolute; left: 159px; width: 340px; }
  .value .body { margin-top: 3px; padding-left: 22px; }

  .team-photo {
    position: absolute; left: 178px; top: 442px; width: 248px; height: 271px;
    border-radius: 40px 40px 20px 20px;
    background: linear-gradient(180deg, var(--photo-a), var(--photo-b));
  }

  .service { position: absolute; left: 710px; width: 400px; }
  .service__icon { position: absolute; left: 0; width: 36px; height: 36px; fill: var(--blue); }
  .service__text { margin-left: 49px; }
  .service .body { margin-top: 9px; }
  .service .heading + .body { margin-top: 2px; }

  .footer-line { position: absolute; left: 0; top: 809px; width: 1200px; height: 2px; background: var(--teal); }
  .page-no { position: absolute; top: 812px; font-size: 9px; color: var(--blue); }
  .page-no--left { left: 65px; }
  .page-no--right { left: 1124px; }
  .contact {
    position: absolute; top: 796px; display: flex; align-items: center; gap: 5px;
    font-size: 9px; color: var(--teal);
  }
  .contact svg { width: 10px; height: 10px; stroke: var(--blue); fill: none; stroke-width: 1.4; }
  .contact--web { left: 346px; }
  .contact--mail { left: 653px; }
</style>
</head>
<body>
<main class="spread">
  <div class="bar bar--left"></div>
  <div class="bar bar--centre"></div>
  <div class="bar bar--right"></div>
  <div class="brand brand--left"><span class="brand__dot"></span>Carewell Staffline</div>
  <div class="brand brand--right"><span class="brand__dot"></span>Carewell Staffline</div>

  <!-- Page 4 -->
  <h1 class="page-title page-title--ethos">Our Ethos</h1>
  <div class="rule rule--ethos"></div>

  <section class="value" style="top:139px">
    <h2 class="heading">HONESTY AND INTEGRITY</h2>
    <p class="body">– We pride ourselves on being direct and straightforward when communicating with our clients and candidates.</p>
  </section>
  <section class="value" style="top:204px">
    <h2 class="heading">DEDICATION</h2>
    <p class="body">– Our consultants aim to fully understand the requirements of our clients and candidates to find mutually beneficial solutions.</p>
  </section>
  <section class="value" style="top:282px">
    <h2 class="heading">SERVICE EXCELLENCE</h2>
    <p class="body">– We aim to always deliver superior services to help both employers and candidates achieve their goals.</p>
  </section>
  <section class="value" style="top:346px">
    <h2 class="heading">LEADERSHIP</h2>
    <p class="body">– Our purpose is to become leaders in the healthcare recruitment sector, raising the bar for the entire industry.</p>
  </section>

  <div class="team-photo" role="img" aria-label="Photo of a team of care staff in light blue uniforms joining hands in a circle"></div>

  <!-- Page 5 -->
  <h1 class="page-title page-title--suggestions">Our suggestions</h1>
  <div class="rule rule--suggestions"></div>

  <section class="service" style="top:139px">
    <svg class="service__icon" viewBox="0 0 36 36" aria-hidden="true" style="top:2px"><path d="M18 3 1 17l3 3 14-11 14 11 3-3z"/><path d="M7 19 18 11l11 8v13H21v-8h-6v8H7z"/></svg>
    <div class="service__text">
      <h2 class="heading">RESIDENTIAL HOMES</h2>
      <p class="body">We work closely with Residential homes in the local area.</p>
      <p class="body">These are permanent care homes for the elderly, adults with learning disabilities and children.</p>
      <p class="body">They may be privately owned or run by charities or councils.</p>
    </div>
  </section>

  <section class="service" style="top:255px">
    <svg class="service__icon" viewBox="0 0 36 42" aria-hidden="true" style="top:3px;height:42px"><path d="M13 0h10v6h9v32h3v3H1v-3h3V6h9zM16 2v3h-3v3h3v3h4V8h3V5h-3V2zM7 9v29h22V9h-4v4H11V9zm4 7h5v5h-5zm9 0h5v5h-5zm-9 8h5v5h-5zm9 0h5v5h-5zm-5 7h6v7h-6z"/></svg>
    <div class="service__text">
      <h2 class="heading">HOSPITALS</h2>
      <p class="body">We supply staff to Private General Hospitals and also work closely with Hospitals specialising in Mental Health Conditions.</p>
      <p class="body">We often place RGN’s into general hospitals but also recruit HCA’s with a clinical skill set to work in the same environment.</p>
      <p class="body">For Mental Health Hospitals, we have a high demand for RMN’s and Support Workers.</p>
    </div>
  </section>

  <section class="service" style="top:414px">
    <svg class="service__icon" viewBox="0 0 36 28" aria-hidden="true" style="top:6px;height:28px"><circle cx="18" cy="6" r="5.5"/><circle cx="6" cy="8" r="4"/><circle cx="30" cy="8" r="4"/><path d="M8 27c0-8 4-13 10-13s10 5 10 13z"/><path d="M0 21c0-5 3-8 7-8 2 0 3 1 4 2-2 2-3 4-3 6z"/><path d="M36 21c0-5-3-8-7-8-2 0-3 1-4 2 2 2 3 4 3 6z"/></svg>
    <div class="service__text">
      <h2 class="heading">SUPPORT WORK</h2>
      <p class="body">This involves supporting individuals who need help emotionally and practically, to help them gain independence and get the most out of life.</p>
      <p class="body">Support work covers an array of areas such as mental health, challenging behaviour, learning disabilities and physical disabilities.</p>
      <p class="body">Service users may be based in a residential home, hospital, supported living environment or a day centre depending on their condition.</p>
    </div>
  </section>

  <section class="service" style="top:602px">
    <svg class="service__icon" viewBox="0 0 36 42" aria-hidden="true" style="top:4px;height:42px"><path d="M3 0h30v39h3v3H0v-3h3zm3 3v36h24V3zm4 5h5v5h-5zm11 0h5v5h-5zm-11 8h5v5h-5zm11 0h5v5h-5zm-11 8h5v5h-5zm11 0h5v5h-5zm-6 8h6v7h-6z"/></svg>
    <div class="service__text">
      <h2 class="heading">NURSING HOMES</h2>
      <p class="body">Nursing Homes are very similar to care homes for the elderly.</p>
      <p class="body">However, the care team on duty will always include at least one qualified nurse.</p>
      <p class="body">Nursing Homes can therefore cater for people with a medical condition that requires nursing attention.</p>
    </div>
  </section>

  <!-- Footer -->
  <div class="footer-line"></div>
  <span class="page-no page-no--left">4</span>
  <span class="page-no page-no--right">5</span>
  <div class="contact contact--web">
    <svg viewBox="0 0 10 10" aria-hidden="true"><circle cx="5" cy="5" r="4.2"/><ellipse cx="5" cy="5" rx="1.8" ry="4.2"/><path d="M1 5h8"/></svg>
    <span>https://www.carewellstaffline.example/</span>
  </div>
  <div class="contact contact--mail">
    <svg viewBox="0 0 12 10" aria-hidden="true" style="width:12px"><rect x="1" y="1.5" width="10" height="7" rx="1"/><path d="m1 2 5 4 5-4"/></svg>
    <span>info@carewellstaffline.example</span>
  </div>
</main>
</body>
</html>
```